Referral Card thats different from the rest

Business card size-

Referral card that will be given to clients, in turn they will pass it on to their friends.

The referee will add their name and address, and friends name to card before it is passed on

Referee gets 2 FREE movie tickets

Friend gets $25 OFF their service

Company is an electrical contracting company specialising in the domestic market.

I would like the card to be fun not so serious!
Completely open minded to any and every creative idea!

attached is 2 photo of an example of what another business has, i am trying to achieve something similiar
Updates

I have increased the budget, ;)

i have added 2 x photos of what i am trying to achieve. this is from another business, I am after something similar to this
Thanks

I have updated the design brief.
this should help make it easir and more clear
Thanks

Target Market(s)

Home owners from 30yrs +

Industry/Entity Type

Electrical

Requirements
Must have
• Logo - Not a main feature of card
1300 574 862 on both sides
Lic no: 381946D (doesn’t have to be big) prefer on back

The main feature of the front of the card is the 2 free movie tickets for Referee & $25 OFF Friends first bill

HOW ABOUT TWO FREE MOVIE TICKETS?
It is easy! Know someone who needs an electrician? Maybe a friend, family member, relative or work colleague.
Tell them about us, and we will take $25 off their first bill and give you two FREE Movie Tickets just for introducing us.
To make a referral fill out this card and give it to your friend.

Recommended By:____________
Address:__________________
Frinds name: _____________

*this offer is only valued for work over $55. Non transferable for cash. This coupon is limited to 1 per customer, not to be used in conjunction with any other offer
Nice to have
• Catchy heading on card
example- tell a friend for cash card, (if i was giving away cash vouchers..)

example- keep me in your wallet and pass me on

```html
<!DOCTYPE html>
<html lang="en">
<head>
<meta charset="utf-8">
<title>The Pass-It-On Card – Spark Ready Electrical</title>
<link rel="stylesheet" href="https://fonts.googleapis.com/css2?family=Federo&family=Dancing+Script:wght@600;700&family=Crimson+Text&display=swap">
<style>
  :root {
    --canvas: #d9d9d9;
    --card-white: #ffffff;
    --card-orange: #ebb283;
    --maroon: #7a1520;
    --maroon-deep: #6b1019;
    --green: #1f6b2c;
    --rule: #555555;
    --mark: #8a7a6a;
  }
  * { box-sizing: border-box; margin: 0; padding: 0; }
  html, body { width: 1200px; height: 728px; overflow: hidden; background: var(--canvas); }
  .sheet { position: relative; width: 1200px; height: 728px; }

  .card { position: absolute; overflow: hidden; background: var(--card-white); }
  .card--front-warm { left: 7px; top: 7px; width: 590px; height: 351px; background: var(--card-orange); }
  .card--front-white { left: 605px; top: 7px; width: 591px; height: 351px; }
  .card--explainer { left: 7px; top: 366px; width: 590px; height: 355px; }
  .card--back { left: 605px; top: 366px; width: 591px; height: 355px; }

  .brand-mark {
    position: absolute; left: 115px; top: 60px; width: 300px; height: 260px;
    display: flex; flex-direction: column; align-items: center; justify-content: center; gap: 14px;
    opacity: 0.14; pointer-events: none;
  }
  .brand-mark__dot { width: 120px; height: 120px; border-radius: 50%; background: var(--mark); }
  .brand-mark__name { font-family: "Federo", sans-serif; font-size: 30px; color: var(--mark); text-align: center; line-height: 1.1; }

  .card__title {
    position: absolute; left: 0; right: 0; top: 24px; text-align: center;
    font-family: "Federo", sans-serif; font-size: 50px; color: var(--maroon);
    -webkit-text-stroke: 0.8px var(--maroon); letter-spacing: 0.5px;
  }
  .offer {
    position: absolute; left: 0; right: 0; text-align: center;
    font-family: "Federo", sans-serif; font-size: 27px; color: var(--maroon);
    -webkit-text-stroke: 0.7px var(--maroon); letter-spacing: 0.3px;
  }
  .offer--referee { top: 126px; }
  .offer--friend { top: 184px; }
  .accent { color: var(--green); -webkit-text-stroke-color: var(--green); }

  .phone {
    position: absolute; left: 0; right: 0; text-align: center;
    font-family: "Federo", sans-serif; font-size: 48px; color: var(--maroon-deep);
    -webkit-text-stroke: 1.4px var(--maroon-deep); letter-spacing: 1px;
  }
  .card--front-warm .phone, .card--front-white .phone { top: 266px; }

  .explainer__lead {
    position: absolute; left: 0; right: 0; top: 105px; text-align: center;
    font-family: "Federo", sans-serif; font-size: 18px; color: var(--maroon);
    -webkit-text-stroke: 0.5px var(--maroon);
  }
  .explainer__body {
    position: absolute; left: 33px; top: 128px; width: 550px;
    font-family: "Dancing Script", cursive; font-weight: 600; font-size: 19px; line-height: 24.5px;
    color: var(--green);
  }
  .card--explainer .phone { top: 266px; }

  .form-label {
    position: absolute; font-family: "Dancing Script", cursive; font-weight: 700; font-size: 21px; color: var(--green);
  }
  .form-label--self { left: 86px; top: 20px; }
  .form-label--referrer { left: 352px; top: 20px; }
  .form-field {
    position: absolute; font-family: "Crimson Text", serif; font-size: 19px; color: var(--green);
    display: flex; align-items: flex-end; gap: 6px;
  }
  .form-field__line { display: inline-block; border-bottom: 1px solid var(--rule); height: 18px; }
  .form-field--self-name { left: 16px; top: 50px; }
  .form-field--ref-name { left: 295px; top: 50px; }
  .form-field--ref-address { left: 295px; top: 78px; }
  .form-field--ref-extra { left: 307px; top: 108px; }

  .back__pitch {
    position: absolute; left: 0; right: 0; top: 156px; text-align: center;
    font-family: "Crimson Text", serif; font-size: 18px; line-height: 23.5px; color: var(--maroon);
  }
  .back__pitch strong { font-weight: 400; -webkit-text-stroke: 0.5px var(--maroon); }
  .card--back .phone { top: 242px; font-size: 38px; -webkit-text-stroke-width: 1.2px; }
  .licence {
    position: absolute; left: 0; right: 0; top: 295px; text-align: center;
    font-family: "Dancing Script", cursive; font-weight: 700; font-size: 13px; color: var(--green);
  }
  .licence__number { font-family: "Crimson Text", serif; font-size: 14px; color: var(--maroon); }
  .terms {
    position: absolute; left: 4px; top: 324px; width: 585px;
    font-family: "Crimson Text", serif; font-size: 11.5px; line-height: 15px; color: var(--maroon);
  }
</style>
</head>
<body>
<main class="sheet">

  <section class="card card--front-warm">
    <div class="brand-mark" role="img" aria-label="Faint Spark Ready Electrical brand mark"><span class="brand-mark__dot"></span><span class="brand-mark__name">Spark Ready Electrical</span></div>
    <h1 class="card__title">The Pass-It-On Card</h1>
    <p class="offer offer--referee">Referee gets <span class="accent">2</span> free movie tickets</p>
    <p class="offer offer--friend">Friend gets <span class="accent">$25</span> off on first bill</p>
    <p class="phone">1300 574 862</p>
  </section>

  <section class="card card--front-white">
    <div class="brand-mark" role="img" aria-label="Faint Spark Ready Electrical brand mark"><span class="brand-mark__dot"></span><span class="brand-mark__name">Spark Ready Electrical</span></div>
    <h2 class="card__title">The Pass-It-On Card</h2>
    <p class="offer offer--referee">Referee gets <span class="accent">2 free</span> movie tickets</p>
    <p class="offer offer--friend">Friend gets <span class="accent">$25</span> off on first bill</p>
    <p class="phone">1300 574 862</p>
  </section>

  <section class="card card--explainer">
    <div class="brand-mark" role="img" aria-label="Faint Spark Ready Electrical brand mark"><span class="brand-mark__dot"></span><span class="brand-mark__name">Spark Ready Electrical</span></div>
    <h2 class="card__title">The Pass-It-On Card</h2>
    <p class="explainer__lead">HOW ABOUT TWO FREE MOVIE TICKETS?</p>
    <p class="explainer__body">It is easy! Know someone who needs an electrician? Maybe a friend, family member, relative or work colleague.<br>Tell them about us, and we will take $25 off their first bill and give you two FREE Movie Tickets just for introducing us.<br>To make a referral fill out this card and give it to your friend.</p>
    <p class="phone">1300 574 862</p>
  </section>

  <section class="card card--back">
    <p class="form-label form-label--self">I am</p>
    <p class="form-label form-label--referrer">I was referred by</p>
    <p class="form-field form-field--self-name">Name: <span class="form-field__line" style="width:172px"></span></p>
    <p class="form-field form-field--ref-name">Name: <span class="form-field__line" style="width:206px"></span></p>
    <p class="form-field form-field--ref-address">Address:<span class="form-field__line" style="width:194px"></span></p>
    <p class="form-field form-field--ref-extra"><span class="form-field__line" style="width:252px"></span></p>
    <p class="back__pitch">If you’re happy with our service, we would really love for you to<br>recommend us to your friends.If your friends use our service we<br>will give you <strong>2 FREE</strong> movie tickets &amp; your friends <strong>$25</strong> OFF their service.</p>
    <p class="phone">1300 574 862</p>
    <p class="licence">Lic Number <span class="licence__number">381946D</span></p>
    <p class="terms">*this offer is only valued for work over $55. Non transferable for cash. This coupon is limited to 1 per customer,<br>&nbsp;not to be used in conjunction with any other offer.</p>
  </section>

</main>
</body>
</html>
```